Redesign of an existing webpage

We've just redesigned our logo on a new website design to reflect the new logo. That wants to change the color and graphical appearance of our website. There are no restrictions on what should be changed. IT should display our portfolio and pricing and explain our product. Please provide stock photos if needed. The site structure should not be changed. So we want the pages which are currently there. We need the following pages: Main page (Home page) Detail page (currently used at AGB and questions) Imprint (including the map) existing webpage: www.brightdune.de
Updates

I've got a request from one of the designers-

Target Market(s)

We are offering IT services to small companies. The do not need own IT equipment or PC Specialists if if our service.

Industry/Entity Type

It Service

Coding

Coded - Design and coding required

Number of Pages Required

3 page

Font styles to use
Other font styles liked:
• Relaway

Colors

Designer to choose colors to be used in the design.

Requirements
Must have
• our login mask at https://desktop.brightdune.com needs a rebranding too

```html
<!DOCTYPE html>
<html lang="en">
<head>
<meta charset="utf-8">
<title>BrightDune – IT that just works</title>
<link href="https://fonts.googleapis.com/css2?family=Raleway:wght@400;500;600;700&display=swap" rel="stylesheet">
<style>
:root{
  --blue:#0f6fc4;
  --blue-dark:#0b4f91;
  --blue-soft:#e3eefa;
  --blue-wash:#eef4fa;
  --ink:#1d1d1f;
  --text:#555b63;
  --muted:#9aa1a9;
  --red:#e84a4a;
  --green:#5cb32b;
  --pink-card:#fde6e8;
  --green-card:#eef7e1;
  --white:#ffffff;
}
*{box-sizing:border-box;margin:0;padding:0}
html,body{width:1200px;height:4388px;overflow:hidden}
body{position:relative;background:var(--white);font-family:"Raleway",sans-serif;color:var(--text)}
.abs{position:absolute}
a{text-decoration:none;color:inherit}

.decor-circle{position:absolute;border-radius:50%;background:var(--blue-wash)}

.brand{position:absolute;left:34px;top:40px;display:flex;align-items:center;gap:12px;font-size:34px;font-weight:600;color:var(--blue);letter-spacing:1px}
.brand-mark{width:22px;height:22px;background:var(--blue)}
.nav{position:absolute;top:48px;left:408px;display:flex;align-items:center;font-size:16px;color:#333}
.nav a{margin-right:46px}
.nav .active{background:var(--blue);color:#fff;font-weight:600;padding:4px 12px}
.nav .cta{margin-left:18px;margin-right:0;background:#fff;color:var(--blue);padding:8px 18px;box-shadow:0 2px 10px rgba(0,0,0,.08);font-size:15px}

.hero-title{left:120px;top:142px;font-size:44px;font-weight:600;color:var(--blue)}
.hero-text{left:120px;top:220px;width:615px;font-size:16.5px;line-height:30px;color:#444}
.btn{display:inline-block;background:var(--blue);color:#fff;font-weight:500}
.hero-btn{left:121px;top:404px;width:193px;height:41px;line-height:41px;text-align:center;font-size:17px;box-shadow:0 6px 14px rgba(15,111,196,.3)}
.know-more{left:364px;top:405px;display:flex;align-items:center;gap:16px;font-size:17px;color:#444}
.hero-art{left:752px;top:128px;width:322px;height:298px;background:radial-gradient(circle at 55% 45%,#bfe0fb 0,#e6f1fc 55%,transparent 72%)}

.section-title{position:absolute;left:0;width:1200px;text-align:center;font-size:30px;font-weight:600;color:var(--ink)}

.card{position:absolute;top:602px;width:326px;height:360px;padding:40px 34px}
.card-icon{width:70px;height:70px;border-radius:8px;background:rgba(255,255,255,.6);margin-bottom:24px}
.card h3{font-size:17px;font-weight:600;color:var(--ink);margin-bottom:22px}
.card p{font-size:13px;line-height:23px;text-align:justify;color:#555}
.learn{display:flex;align-items:center;gap:16px;font-size:13px;font-weight:600;margin-top:20px}
.card.pink{left:97px;background:var(--pink-card)}
.card.pink .learn{color:var(--red)}
.card.green{left:438px;background:var(--green-card)}
.card.green .learn{color:var(--green)}
.card.blue{left:779px;background:var(--blue-soft)}
.card.blue .learn{color:var(--blue)}

.down-btn{left:617px;top:992px;width:68px;height:68px;border-radius:50%;background:#fff;box-shadow:0 6px 20px rgba(0,0,0,.1);display:flex;align-items:center;justify-content:center}

.benefits-title{left:36px;top:1100px;font-size:31px;font-weight:600;color:var(--ink)}
.benefits-text{left:34px;top:1162px;width:486px;font-size:12.8px;line-height:30.5px;text-align:justify;color:#444}
.benefits-learn{left:34px;top:1404px;color:var(--blue)}
.benefit{position:absolute;width:220px;text-align:center;font-size:16px;font-weight:600;color:var(--ink)}
.benefit-icon{width:100px;height:100px;margin:0 auto 18px;border-radius:14px;background:var(--blue-soft)}

.customer-band{left:0;top:1510px;width:1200px;height:533px;background:var(--blue-wash)}
.customer-sub{left:0;top:1607px;width:1200px;text-align:center;font-size:12.5px;color:var(--blue)}
.customer-art{left:34px;top:1688px;width:478px;height:298px;border-radius:12px;background:linear-gradient(135deg,#d6e7f8,#f4e7d2 60%,#e3eefa)}
.step{position:absolute;left:580px;width:590px}
.step-num{position:absolute;left:0;top:0;width:36px;height:36px;border-radius:50%;color:#fff;font-size:12px;font-weight:700;display:flex;align-items:center;justify-content:center}
.step h4{margin-left:68px;font-size:15px;font-weight:600;color:var(--ink);margin-bottom:12px}
.step p{margin-left:68px;font-size:13px;line-height:19px;color:#555}

.service-diamond{left:-140px;top:2160px;width:430px;height:430px;transform:rotate(45deg);background:var(--blue-wash);border-radius:40px}
.service-title{left:34px;top:2238px;font-size:27px;font-weight:600;color:var(--ink)}
.service-text{left:34px;top:2292px;width:285px;font-size:12.5px;line-height:27px;text-align:justify;color:#444}
.service-learn{left:34px;top:2514px;color:var(--blue)}
.plan{position:absolute;top:2194px;width:227px;height:409px;border:2px solid var(--blue);background:#fff;text-align:center}
.plan.green{border-color:var(--green)}
.plan-ribbon{position:absolute;left:-2px;top:-2px}
.plan-name{position:relative;margin-top:8px;font-size:12px;font-weight:700;color:#fff;letter-spacing:.3px}
.plan-art{width:86px;height:60px;margin:48px auto 18px;border-radius:6px;background:linear-gradient(180deg,#d9e8f7,#f1e2c7)}
.plan-price{font-size:33px;font-weight:700;color:var(--ink)}
.plan-per{font-size:12.5px;color:var(--blue);margin:10px 0 8px}
.plan.green .plan-per{color:var(--green)}
.plan ul{list-style:none;text-align:left;padding-left:16px}
.plan li{font-size:11px;color:var(--muted);line-height:27px;display:flex;align-items:center;gap:16px}
.plan li b{color:var(--blue);font-size:11px}
.plan.green li b{color:var(--green)}
.plan-btn{display:inline-block;margin-top:14px;width:126px;height:29px;line-height:29px;font-size:11.5px;font-weight:600;color:#fff;background:var(--blue)}
.plan.green .plan-btn{background:var(--green)}

.simple-title{left:36px;top:2740px;font-size:33px;font-weight:600;color:var(--ink)}
.simple-text{left:36px;top:2810px;width:564px;font-size:15.5px;line-height:31px;text-align:justify;color:var(--muted)}
.network-art{left:725px;top:2719px;width:451px;height:290px;border-radius:10px;background:linear-gradient(135deg,#dbeaf8,#f3f7fb)}

.testi-diamond{left:790px;top:3060px;width:400px;height:400px;transform:rotate(45deg);background:var(--blue-wash);border-radius:50px}
.testi-title{left:124px;top:3176px;font-size:31px;font-weight:600;color:var(--ink)}
.testi-role{left:122px;top:3262px;font-size:22px;font-weight:600;color:var(--blue)}
.testi-quote{left:122px;top:3310px;width:380px;font-size:12.5px;line-height:21px;color:#555}
.avatar{position:absolute;border-radius:50%;background:linear-gradient(160deg,#c9a58a,#6f5a4c)}
.testi-name{left:217px;top:3397px;font-size:15px;font-weight:600;color:var(--ink)}
.testi-job{left:217px;top:3420px;font-size:12.5px;color:var(--muted)}
.testi-arrows{left:122px;top:3474px;display:flex;gap:14px}

.founders-band{left:0;top:3637px;width:1200px;height:535px;background:var(--blue-wash)}
.founders-text{left:140px;top:3742px;width:920px;text-align:center;font-size:13.5px;line-height:26px;color:#444}
.founder{position:absolute;top:3835px;width:363px;height:308px;background:#fff;padding:26px 16px}
.founder-photo{position:absolute;left:26px;top:26px;width:92px;height:92px;border-radius:50%;background:linear-gradient(160deg,#e3c2a5,#8a6a58)}
.founder h4{margin-left:126px;margin-top:20px;font-size:15.5px;font-weight:600;color:var(--ink)}
.founder .role{margin-left:126px;margin-top:10px;font-size:13px;color:var(--muted)}
.founder .bio{margin-top:58px;font-size:11px;line-height:21px;text-align:justify;color:#555}
.founder .quote{font-size:11px;line-height:21px;font-style:italic;color:var(--blue);margin-top:2px}
.founder .learn{color:var(--blue);margin-top:14px}

.foot-col{position:absolute;top:4226px}
.foot-brand{font-size:17px;font-weight:600;color:var(--ink)}
.foot-head{font-size:13.5px;font-weight:600;color:var(--ink)}
.foot-col .small{font-size:12px;color:var(--muted);line-height:26px}
.foot-phone{font-size:12px;font-weight:700;color:var(--blue)}
.socials{display:flex;gap:9px;margin-top:16px}
.socials span{width:16px;height:16px;background:var(--blue);display:block}
</style>
</head>
<body>

<div class="decor-circle" style="left:-240px;top:-280px;width:720px;height:843px"></div>
<div class="decor-circle" style="left:1015px;top:410px;width:400px;height:400px"></div>
<div class="decor-circle" style="left:-60px;top:1025px;width:190px;height:190px"></div>

<header>
  <a class="brand" href="#"><span class="brand-mark"></span>BrightDune</a>
  <nav class="nav">
    <a class="active" href="#">Home</a>
    <a href="#">That's How it's Done</a>
    <a href="#">Prices</a>
    <a href="#">About Us</a>
    <a href="#">Ask</a>
    <a class="cta" href="#">Get Started Now</a>
  </nav>
</header>

<section class="hero">
  <h1 class="abs hero-title">Just work.</h1>
  <p class="abs hero-text">In large companies, IT departments ensure a functioning IT. Central servers are used, which are accessed from the individual workstations.</p>
  <a class="abs btn hero-btn" href="#">Get Started Learn</a>
  <a class="abs know-more" href="#">
    <svg width="40" height="40" viewBox="0 0 40 40"><circle cx="20" cy="20" r="18" fill="none" stroke="#888" stroke-width="1.6"/><path d="M16 13 L27 20 L16 27 Z" fill="none" stroke="#888" stroke-width="1.6"/></svg>
    Know More
  </a>
  <div class="abs hero-art" role="img" aria-label="Isometric illustration of a central data center connected to server racks"></div>
</section>

<section>
  <h2 class="section-title" style="top:510px">IT that just works</h2>
  <article class="card pink">
    <div class="card-icon" role="img" aria-label="Icon of a light bulb on a laptop"></div>
    <h3>The problem</h3>
    <p>The basis of the IT problems that unnecessarily complicate your daily business is - in addition to the human factor - the computer itself.</p>
    <a class="learn" href="#">Learn More <svg width="28" height="14" viewBox="0 0 28 14"><path d="M0 7H26M20 1L26 7L20 13" fill="none" stroke="currentColor" stroke-width="2"/></svg></a>
  </article>
  <article class="card green">
    <div class="card-icon" role="img" aria-label="Icon of a hand holding a gear"></div>
    <h3>our solution</h3>
    <p>BrightDune provides you with a solution that ensures the daily backup of your data and the monitoring of the operational readiness of your system.</p>
    <a class="learn" href="#">Learn More <svg width="28" height="14" viewBox="0 0 28 14"><path d="M0 7H26M20 1L26 7L20 13" fill="none" stroke="currentColor" stroke-width="2"/></svg></a>
  </article>
  <article class="card blue">
    <div class="card-icon" role="img" aria-label="Icon of a globe above a rated laptop"></div>
    <h3>Your safety</h3>
    <p>If you're wondering how secure our solution is, the answer is simple: very safe. We work with Nordvault, one of Germany's largest data centers.</p>
    <a class="learn" href="#">Learn More <svg width="28" height="14" viewBox="0 0 28 14"><path d="M0 7H26M20 1L26 7L20 13" fill="none" stroke="currentColor" stroke-width="2"/></svg></a>
  </article>
  <a class="abs down-btn" href="#" aria-label="Scroll down">
    <svg width="22" height="28" viewBox="0 0 22 28"><path d="M11 1V26M3 18L11 26L19 18" fill="none" stroke="#0f6fc4" stroke-width="2.4"/></svg>
  </a>
</section>

<section>
  <h2 class="abs benefits-title">Your benefits at a glance</h2>
  <p class="abs benefits-text">Explode resources for your core business, because you do not have to worry about time-consuming malfunctions such as lame programs, virus attacks, data loss, etc., nor do you have to book an external service provider for rectification. Capacity and storage issues are a thing of the past, and your operating system is updated by the data center - faster, more direct, and much safer than what you could do on-site. If you use our ThinClients, further investments in your EDP infrastructure will be avoided.</p>
  <a class="abs learn benefits-learn" href="#">Learn More <svg width="28" height="14" viewBox="0 0 28 14"><path d="M0 7H26M20 1L26 7L20 13" fill="none" stroke="currentColor" stroke-width="2"/></svg></a>

  <div class="benefit" style="left:541px;top:1117px"><div class="benefit-icon" role="img" aria-label="Icon of a delivery truck"></div>Express suppression</div>
  <div class="benefit" style="left:761px;top:1117px"><div class="benefit-icon" role="img" aria-label="Icon of a magnifier over a display"></div>Fast programs</div>
  <div class="benefit" style="left:974px;top:1117px"><div class="benefit-icon" role="img" aria-label="Icon of a database with a refresh arrow"></div>data backup</div>
  <div class="benefit" style="left:541px;top:1292px"><div class="benefit-icon" role="img" aria-label="Icon of a briefcase"></div>Professional protection</div>
  <div class="benefit" style="left:761px;top:1292px"><div class="benefit-icon" role="img" aria-label="Icon of a light bulb"></div>sustained</div>
  <div class="benefit" style="left:974px;top:1292px"><div class="benefit-icon" role="img" aria-label="Icon of a shield with a lock"></div>High security</div>
</section>

<section>
  <div class="abs customer-band"></div>
  <h2 class="section-title" style="top:1554px">How do I become a customer?</h2>
  <p class="abs customer-sub">To become a BrightDune customer requires the following four steps.</p>
  <div class="abs customer-art" role="img" aria-label="Illustration of people working around a large security shield with coins and a laptop"></div>
  <div class="step" style="top:1655px"><span class="step-num" style="background:#e84a4a">1</span><h4>Select service</h4><p>BrightDune offers two different models. Choose one of these models.</p></div>
  <div class="step" style="top:1747px"><span class="step-num" style="background:#2d8fe0">2</span><h4>Send an inquiry</h4><p>Fill out our form for a contract request without obligation. We evaluate the feasibility and draft a contract.</p></div>
  <div class="step" style="top:1846px"><span class="step-num" style="background:#5cb32b">3</span><h4>sign a contract</h4><p>The signed contract can be sent to us by post or by e-mail.</p></div>
  <div class="step" style="top:1939px"><span class="step-num" style="background:#f19a9a">4</span><h4>work loose</h4><p>Once the contract has been entered, you can start work within five working days.</p></div>
</section>

<section>
  <div class="abs service-diamond"></div>
  <h2 class="abs service-title">Select service</h2>
  <p class="abs service-text">Choose your service. BrightDune provides a complete workstation in the Thin Client model . All you need is a monitor to get started.<br><br>Both services can be encrypted using an existing PC, laptop or tablet from any location.</p>
  <a class="abs learn service-learn" href="#">Learn More <svg width="28" height="14" viewBox="0 0 28 14"><path d="M0 7H26M20 1L26 7L20 13" fill="none" stroke="currentColor" stroke-width="2"/></svg></a>

  <article class="plan" style="left:529px">
    <svg class="plan-ribbon" width="227" height="40" viewBox="0 0 227 40"><path d="M0 0H227V24L113.5 40L0 24Z" fill="#0f6fc4"/></svg>
    <div class="plan-name">THIN CLIENT</div>
    <div class="plan-art" role="img" aria-label="Illustration of a person working at a desk"></div>
    <div class="plan-price">from 99 €</div>
    <div class="plan-per">per user / month (from 5 users)</div>
    <ul>
      <li><b>»</b>up to 5 users 115 € / month</li>
      <li><b>»</b>Minimum term 12 months</li>
      <li><b>»</b>Thinclient per user included</li>
      <li><b>»</b>Max. 8 hours reaction time</li>
    </ul>
    <a class="plan-btn" href="#">Get Start Now</a>
  </article>
  <article class="plan green" style="left:864px">
    <svg class="plan-ribbon" width="227" height="40" viewBox="0 0 227 40"><path d="M0 0H227V24L113.5 40L0 24Z" fill="#5cb32b"/></svg>
    <div class="plan-name">BRING YOUR OWN</div>
    <div class="plan-art" role="img" aria-label="Illustration of a person working at a desk"></div>
    <div class="plan-price">from 75 €</div>
    <div class="plan-per">per user / month (from 5 users)</div>
    <ul>
      <li><b>»</b>up to 5 users 115 € / month</li>
      <li><b>»</b>No minimum term</li>
      <li><b>»</b>Use with own terminal</li>
      <li><b>»</b>Max. 8 hours reaction time</li>
    </ul>
    <a class="plan-btn" href="#">Get Start Now</a>
  </article>
</section>

<section>
  <h2 class="abs simple-title">Simple, reliable and cheap</h2>
  <p class="abs simple-text">Big companies have been working this way for years, cutting costs and improving stability. Now BrightDune offers the solution for even the smallest businesses. We store your data permanently in a safe place. Necessary security measures are taken, your data is backed up and you focus on your daily business.</p>
  <div class="abs network-art" role="img" aria-label="Network diagram: IP cameras, remote control, monitor, server, thin client, mobile client and mouse connected through a switch"></div>
</section>

<section>
  <div class="abs testi-diamond"></div>
  <div class="avatar" style="left:1043px;top:3106px;width:72px;height:72px" role="img" aria-label="Customer portrait"></div>
  <div class="avatar" style="left:852px;top:3212px;width:72px;height:72px" role="img" aria-label="Customer portrait"></div>
  <div class="avatar" style="left:1016px;top:3260px;width:72px;height:72px" role="img" aria-label="Customer portrait"></div>
  <div class="avatar" style="left:914px;top:3396px;width:72px;height:72px" role="img" aria-label="Customer portrait"></div>
  <div class="avatar" style="left:1074px;top:3396px;width:72px;height:72px" role="img" aria-label="Customer portrait"></div>

  <h2 class="abs testi-title">What our customers say</h2>
  <h3 class="abs testi-role">Hausverwalter</h3>
  <p class="abs testi-quote">"I'm able to work everywhere. Competitors had to file for bankruptcy after a cryptovirus. My data is safe. "</p>
  <div class="avatar" style="left:122px;top:3382px;width:62px;height:62px" role="img" aria-label="Portrait of the quoted customer"></div>
  <div class="abs testi-name">Peter Hollweg</div>
  <div class="abs testi-job">Hausverwalter</div>
  <div class="abs testi-arrows">
    <svg width="20" height="12" viewBox="0 0 20 12"><path d="M20 6H2M7 1L2 6L7 11" fill="none" stroke="#555" stroke-width="1.6"/></svg>
    <svg width="20" height="12" viewBox="0 0 20 12"><path d="M0 6H18M13 1L18 6L13 11" fill="none" stroke="#555" stroke-width="1.6"/></svg>
  </div>
</section>

<section>
  <div class="abs founders-band"></div>
  <div class="decor-circle" style="left:1060px;top:3970px;width:240px;height:240px;background:#fff"></div>
  <div class="decor-circle" style="left:1090px;top:4000px;width:180px;height:180px;background:var(--blue-wash)"></div>
  <h2 class="section-title" style="top:3682px">The founders</h2>
  <p class="abs founders-text">The company BrightDune was founded on 18.03.2019 by Jonas Kettler and Lukas Brenner. The foundation was preceded by a two-year test and design phase. The headquarters of the company is located on the tranquil Lindensee.</p>

  <article class="founder" style="left:152px">
    <div class="founder-photo" role="img" aria-label="Portrait of Lukas Brenner"></div>
    <h4>Lukas Brenner</h4>
    <div class="role">Founder and CEO</div>
    <p class="bio">Lukas is 46 years old, married and has two children. He has been working in IT for 19 years now and, as a trained merchant,</p>
    <p class="quote">" My goal with BrightDune is to increase the value of IT services in the smallest companies. "</p>
    <a class="learn" href="#">Learn More <svg width="28" height="14" viewBox="0 0 28 14"><path d="M0 7H26M20 1L26 7L20 13" fill="none" stroke="currentColor" stroke-width="2"/></svg></a>
  </article>
  <article class="founder" style="left:679px">
    <div class="founder-photo" role="img" aria-label="Portrait of Jonas Kettler"></div>
    <h4>Jonas Kettler</h4>
    <div class="role">Founder and CEO</div>
    <p class="bio">Jonas is 34 years old and single. He has been working in the computer industry for more than 15 years since his training as a computer specialist and his degree in IT.</p>
    <p class="quote">" My goal with BrightDune is to make IT more secure for the smallest businesses. "</p>
    <a class="learn" href="#">Learn More <svg width="28" height="14" viewBox="0 0 28 14"><path d="M0 7H26M20 1L26 7L20 13" fill="none" stroke="currentColor" stroke-width="2"/></svg></a>
  </article>
</section>

<footer>
  <div class="decor-circle" style="left:-40px;top:4300px;width:130px;height:130px"></div>
  <div class="decor-circle" style="left:1050px;top:4240px;width:30px;height:30px"></div>
  <div class="foot-col" style="left:153px">
    <div class="foot-brand">BrightDune</div>
    <div class="small" style="margin-top:10px">hello@brightdune.example</div>
    <div class="foot-phone">800 - 5550-123</div>
  </div>
  <div class="foot-col" style="left:387px">
    <div class="foot-head">Quick Links</div>
    <div class="small" style="margin-top:6px">Home<br>That's How It's Done<br>Prices<br>About Us</div>
  </div>
  <div class="foot-col" style="left:645px">
    <div class="foot-head">Follow Us</div>
    <div class="socials" aria-label="Social profiles"><span></span><span></span><span></span><span></span><span></span><span></span></div>
    <div style="margin-top:22px;font-size:13px;color:#444">© 2019 BrightDune.</div>
  </div>
</footer>

</body>
</html>
```